Newsletter template

I am looking for 2 newsletter templates. My website is in Wordpress and I want to use in mailchimp for lists.

One newsletter is for local clients of design remodeling firm to be sent monthly

Second newsletter is for web store offerings to be sent weekly.

Target Market(s)

Luxury home and leisure

Industry/Entity Type

Store

Requirements
Must have
• Use logos and colors to seamlessly integrate with website,

```html
<!DOCTYPE html>
<html lang="en">
<head>
<meta charset="utf-8">
<title>Maren Lowe Fine Living Newsletter</title>
<link href="https://fonts.googleapis.com/css2?family=Open+Sans:wght@400;600;700;800&family=Oswald:wght@500;600&display=swap" rel="stylesheet">
<style>
  :root {
    --cyan: #27b4d9;
    --ink: #1d1d1d;
    --body: #3a3a3a;
    --band: #e2e2e2;
    --paper: #f2f2f2;
    --white: #ffffff;
    --hero-light: #a9a8a4;
    --hero-dark: #262626;
  }
  * { margin: 0; padding: 0; box-sizing: border-box; }
  html, body { width: 1200px; height: 2304px; overflow: hidden; }
  body { background: var(--white); font-family: "Open Sans", Arial, sans-serif; color: var(--body); position: relative; }

  .masthead { position: absolute; top: 0; left: 0; width: 1200px; height: 320px; background: var(--white); }
  .brand { position: absolute; left: 60px; top: 40px; font-weight: 700; font-size: 34px; color: var(--cyan); line-height: 1; letter-spacing: 0.3px; }
  .browser-note { position: absolute; right: 60px; top: 50px; font-size: 13px; font-weight: 700; color: var(--ink); letter-spacing: 0.3px; }
  .browser-note span { color: var(--cyan); font-weight: 600; }
  .main-nav { position: absolute; top: 205px; left: 0; width: 1200px; display: flex; justify-content: center; gap: 66px; font-weight: 700; font-size: 27px; color: var(--ink); letter-spacing: 0.5px; }

  .tagline { position: absolute; top: 320px; left: 0; width: 1200px; height: 90px; background: var(--band); display: flex; align-items: center; justify-content: center; font-weight: 800; font-size: 42px; color: var(--ink); letter-spacing: 0.5px; }

  .hero { position: absolute; top: 410px; left: 0; width: 1200px; height: 420px;
    background: linear-gradient(180deg, var(--hero-light) 0%, #8a8985 30%, #4b4a48 62%, var(--hero-dark) 100%); }
  .hero-offer { position: absolute; left: 580px; top: 150px; width: 420px; text-align: center; color: var(--white); font-family: "Oswald", "Arial Narrow", sans-serif; }
  .hero-offer h2 { font-size: 52px; font-weight: 600; line-height: 1.05; letter-spacing: 1px; }
  .hero-offer .collection { position: relative; margin-top: 10px; background: var(--cyan); font-size: 30px; font-weight: 500; padding: 2px 0; letter-spacing: 1px; }
  .hero-offer .badge { position: absolute; left: -4px; top: -26px; background: var(--cyan); font-size: 18px; padding: 0 10px; }
  .hero-offer p { font-size: 30px; font-weight: 500; line-height: 1.15; margin-top: 10px; letter-spacing: 0.5px; }

  .shop { position: absolute; top: 830px; left: 0; width: 1200px; height: 660px; background: var(--paper); }
  .shop h2 { position: absolute; left: 72px; top: 110px; font-size: 50px; font-weight: 800; color: var(--ink); letter-spacing: 0.5px; }
  .shop-copy { position: absolute; left: 72px; top: 195px; width: 660px; font-size: 22px; line-height: 30px; color: var(--body); }
  .shop-copy p + p { margin-top: 30px; }
  .shop-visual { position: absolute; left: 770px; top: 230px; width: 400px; height: 400px; border-radius: 50%;
    border: 8px solid var(--white); background: radial-gradient(circle at 45% 40%, #f7f7f7 0%, #cfe7ee 45%, #8fb8c4 100%); }

  .services { position: absolute; top: 1490px; left: 0; width: 1200px; height: 440px; display: flex; gap: 32px; padding: 60px 60px 0; }
  .service { flex: 1; position: relative; }
  .service h3 { font-size: 26px; font-weight: 700; color: var(--cyan); letter-spacing: 0.5px; margin-bottom: 8px; }
  .service p { font-size: 17px; line-height: 23px; text-align: justify; color: var(--body); }
  .service .more { position: absolute; right: 0; top: 330px; font-size: 18px; font-weight: 700; color: var(--cyan); }

  .footer { position: absolute; top: 1930px; left: 0; width: 1200px; height: 374px; background: var(--band); text-align: center; }
  .footer .brand { position: static; display: inline-block; margin-top: 50px; font-size: 38px; }
  .footer .mission { width: 1100px; margin: 34px auto 0; font-size: 16px; font-weight: 600; color: var(--ink); line-height: 24px; letter-spacing: 0.3px; }
  .social { display: flex; justify-content: center; gap: 30px; margin-top: 40px; }
  .social span { width: 58px; height: 58px; border-radius: 50%; background: var(--cyan); }
  .copyright { margin-top: 30px; font-size: 14px; font-weight: 600; color: var(--ink); letter-spacing: 0.3px; }
</style>
</head>
<body>
  <header class="masthead">
    <div class="brand">Maren Lowe Fine Living</div>
    <div class="browser-note">HAVING TROUBLE READING THIS EMAIL? <span>VIEW THIS EMAIL IN YOUR BROWSER.</span></div>
    <nav class="main-nav"><span>STYLE</span><span>SHOP</span><span>DESIGN</span><span>LIFE</span><span>HOME</span><span>PRESS</span><span>CONTACT</span></nav>
  </header>

  <div class="tagline">WHERE REAL LIFE MEETS REAL STYLE</div>

  <section class="hero" role="img" aria-label="Photo of a modern bathroom with dark teak vanity and concrete wall">
    <div class="hero-offer">
      <h2>INTRODUCING SERENO</h2>
      <div class="collection"><span class="badge">NEW</span>TEAK COLLECTION</div>
      <p>COMPLIMENT YOUR SPA<br>OR BATH</p>
    </div>
  </section>

  <section class="shop">
    <h2>SHOP MAREN LOWE</h2>
    <div class="shop-copy">
      <p>Maren Lowe Fine Living is all about a relaxed, warm and welcoming lifestyle. We have handpicked items that enhance this lifestyle, and allow you to let your personal style shine through.</p>
      <p>Explore our style and safety that our spa bathroom products can bring to your home. Our kitchen and entertaining items will surely set you apart as a welcoming hostess. You will also find an incredible selection of unique and tasteful gifts for everyone on your list.</p>
      <p>You will find designer notes throughout the site to give you extra product information and make your shopping choices easier.</p>
    </div>
    <div class="shop-visual" role="img" aria-label="Circular preview of the online store product pages"></div>
  </section>

  <section class="services">
    <article class="service">
      <h3>DESIGN SERVICES</h3>
      <p>From Blueprints to Bubbles...The design process is fun and exciting without being overwhelming. We help clients create a home that reflects their own personal style. Whether we are purchasing new decor pieces, highlighting discoveries from past travel adventures, or weaving in cherished personal possessions, it is our goal to make sure our clients find their perfect balance between style and function.</p>
      <span class="more">READ MORE &gt;</span>
    </article>
    <article class="service">
      <h3>CONCIERGE SERVICES</h3>
      <p>Whether our clients are here for the season or just a long weekend, we provide the ease and comfort of having concierge services available to help with everything from dinner reservations, fishing excursions, babysitting and refrigerator stocking. It is our goal to make you and your guests' time in Naples extra special. Open the front door and enjoy!</p>
      <span class="more">READ MORE &gt;</span>
    </article>
    <article class="service">
      <h3>HOME MANAGE MENT</h3>
      <p>Properly maintaining homes of exceptional quality and value is a year round job. We take the stress out of this process making our clients' arrivals and departures throughout the year as relaxed and enjoyable. Our team makes sure that all mechanical maintenance, deep cleaning, and regular repairs are performed on a regular basis. Let us take care of the details while you are on the golf course or enjoying the beach.</p>
      <span class="more">READ MORE &gt;</span>
    </article>
  </section>

  <footer class="footer">
    <div class="brand">Maren Lowe Fine Living</div>
    <p class="mission">MAREN LOWE FINE LIVING IS ALL ABOUT A RELAXED, WARM AND WELCOMING LIFESTYLE. WE HAVE HANDPICKED ITEMS THAT ENHANCE THIS LIFESTYLE AND ALLOW YOU TO LET YOUR PERSONAL STYLE SHINE THROUGH.</p>
    <div class="social"><span></span><span></span><span></span><span></span></div>
    <p class="copyright">&copy; 2015 COPYRIGHT MAREN LOWE ENTERPRISES &amp; MAREN LOWE FINE LIVING. ALL RIGHTS RESERVED.</p>
  </footer>
</body>
</html>
```